Bref créative |
Tern Ledger | ||
Business Cards and Letterheads | ||
Use standard fonts | ||
Cutting-Edge Professional Simple |
Ronald Pyke | ||
Suite 412, Level 4, 35 Gorse St, Sydney, NSW, 2000 | ||
ronald@ternledger-example.com | ||
www.ternledger-example.com | ||
Good Luck! | ||
<< Up to the designer >> | ||

```html
<!DOCTYPE html>
<html lang="en">
<head>
<meta charset="utf-8">
<title>Tern Ledger — Stationery</title>
<link rel="stylesheet" href="https://fonts.googleapis.com/css2?family=Arimo:wght@400;700&display=swap">
<style>
  :root {
    --backdrop: #1c1c1e;
    --paper: #ffffff;
    --ink: #1a1a1a;
    --muted: #6b6b6b;
    --orange: #f28a1e;
    --orange-deep: #e47712;
    --rule: #d9d9d9;
  }
  * { box-sizing: border-box; margin: 0; padding: 0; }
  html, body { width: 1200px; height: 706px; overflow: hidden; }
  body {
    background: var(--backdrop);
    font-family: "Arimo", Arial, sans-serif;
    color: var(--ink);
    position: relative;
  }
  .sheet { position: absolute; background: var(--paper); overflow: hidden; }

  /* wordmark */
  .wordmark { display: flex; align-items: center; gap: 6px; font-weight: 700; color: var(--ink); letter-spacing: .02em; }
  .wordmark-dot { width: 12px; height: 12px; border-radius: 50%; background: var(--orange); flex: none; }

  .small { font-size: 7px; line-height: 1.45; color: var(--muted); }

  /* letterhead */
  .letterhead { left: 120px; top: 130px; width: 380px; height: 537px; }
  .letterhead-header { position: absolute; left: 30px; right: 30px; top: 28px; display: flex; justify-content: space-between; align-items: flex-end; }
  .letterhead .wordmark { font-size: 15px; }
  .letterhead-rule { position: absolute; left: 30px; right: 30px; top: 74px; height: 2px; background: var(--orange); }
  .letterhead-footer { position: absolute; left: 0; bottom: 0; width: 100%; height: 60px; }
  .letterhead-url { position: absolute; left: 0; right: 0; bottom: 10px; text-align: center; font-size: 7px; color: #fff; letter-spacing: .04em; }

  /* business cards */
  .card { top: 24px; width: 216px; height: 120px; }
  .card-front { left: 560px; display: flex; flex-direction: column; align-items: center; justify-content: center; gap: 6px; }
  .card-front .wordmark { font-size: 14px; }
  .card-back { left: 796px; padding: 16px 16px; }
  .card-name { font-size: 10px; font-weight: 700; color: var(--orange); }
  .card-title { font-size: 7px; color: var(--muted); margin-bottom: 14px; }
  .card-details { position: absolute; right: 16px; bottom: 14px; text-align: right; }
  .card-details .accent { color: var(--orange); }

  /* envelope back */
  .envelope-back { left: 540px; top: 166px; width: 520px; height: 228px; }
  .envelope-back-flap { position: absolute; left: 0; top: 0; width: 100%; height: 100%; }
  .envelope-back-mark { position: absolute; left: 24px; top: 20px; transform: rotate(180deg); font-size: 14px; color: var(--paper); }
  .envelope-back-mark .wordmark-dot { background: var(--paper); }
  .envelope-back-mark .wordmark { color: var(--paper); }
  .envelope-back-return { position: absolute; right: 24px; top: 22px; text-align: right; color: #fff; transform: rotate(180deg); }

  /* envelope front */
  .envelope-front { left: 540px; top: 412px; width: 520px; height: 255px; border: 1px solid var(--rule); }
  .envelope-tab { position: absolute; top: 14px; width: 14px; height: 32px; background: var(--orange); }
  .envelope-tab.left { left: 0; }
  .envelope-tab.right { right: 0; }
  .envelope-return { position: absolute; left: 30px; top: 18px; }
  .envelope-front .wordmark { position: absolute; right: 40px; top: 112px; font-size: 15px; }
  .envelope-front-rule { position: absolute; left: 30px; right: 30px; bottom: 26px; height: 1px; background: var(--rule); }
</style>
</head>
<body>

  <section class="sheet letterhead" aria-label="Letterhead">
    <header class="letterhead-header">
      <address class="small" style="font-style:normal">
        Suite 412, Level 4, 35 Gorse St<br>
        Sydney, NSW, 2000<br>
        Tel +61 2 5550 0142 &nbsp; Fax +61 2 5550 0143<br>
        ronald@ternledger-example.com
      </address>
      <div class="wordmark"><span class="wordmark-dot"></span>Tern Ledger</div>
    </header>
    <div class="letterhead-rule"></div>
    <svg class="letterhead-footer" viewBox="0 0 380 60" preserveAspectRatio="none" aria-hidden="true">
      <path d="M0 22 Q190 -6 380 22 L380 60 L0 60 Z" fill="var(--orange)"/>
      <path d="M0 26 Q190 2 380 26" fill="none" stroke="var(--orange-deep)" stroke-width="1"/>
    </svg>
    <p class="letterhead-url">www.ternledger-example.com</p>
  </section>

  <section class="sheet card card-front" aria-label="Business card, front">
    <div class="wordmark"><span class="wordmark-dot"></span>Tern Ledger</div>
    <p class="small">www.ternledger-example.com</p>
  </section>

  <section class="sheet card card-back" aria-label="Business card, back">
    <p class="card-name">Ronald Pyke</p>
    <p class="card-title">Managing Director</p>
    <div class="card-details small">
      Suite 412, Level 4, 35 Gorse St<br>
      Sydney, NSW, 2000<br>
      T +61 2 5550 0142<br>
      M +61 400 555 018<br>
      <span class="accent">ronald@ternledger-example.com</span>
    </div>
  </section>

  <section class="sheet envelope-back" aria-label="Envelope, back">
    <svg class="envelope-back-flap" viewBox="0 0 520 228" preserveAspectRatio="none" aria-hidden="true">
      <rect x="0" y="0" width="520" height="70" fill="var(--orange)"/>
      <rect x="0" y="70" width="520" height="2" fill="var(--orange-deep)"/>
    </svg>
    <div class="envelope-back-mark"><div class="wordmark"><span class="wordmark-dot"></span>Tern Ledger</div></div>
    <address class="envelope-back-return small" style="font-style:normal;color:#fff">
      Suite 412, Level 4, 35 Gorse St<br>
      Sydney, NSW, 2000
    </address>
  </section>

  <section class="sheet envelope-front" aria-label="Envelope, front">
    <span class="envelope-tab left"></span>
    <span class="envelope-tab right"></span>
    <address class="envelope-return small" style="font-style:normal">
      Suite 412, Level 4, 35 Gorse St<br>
      Sydney, NSW, 2000<br>
      Tel +61 2 5550 0142 &nbsp; Fax +61 2 5550 0143<br>
      www.ternledger-example.com
    </address>
    <div class="wordmark"><span class="wordmark-dot"></span>Tern Ledger</div>
    <div class="envelope-front-rule"></div>
  </section>

</body>
</html>
```